service truck wrap For KM Fabworks

i want a simple wrap for my work truck,i do mobile welding,Steel fabrication,machining,line boring, industrial maintenance,
I want to cover the entire cube (sides and back) and maybe some info on th truck but not a full wrap

i want to put my logo in the design and my phone numer, with all my offered services
I will add more detail like my logo tomorrow

Target Market(s)

industrial

Industry/Entity Type

welding , machining, industrial maintenance

Requirements
Must have
• business name: KM Fabworks , my Phone number 506-817-2296, my logo

```html
<!DOCTYPE html>
<html lang="fr">
<head>
<meta charset="utf-8">
<title>KM Fabworks — Service Truck Wrap</title>
<link rel="stylesheet" href="https://fonts.googleapis.com/css2?family=Open+Sans:wght@700&family=Roboto+Condensed:wght@400&display=swap">
<style>
  :root {
    --wrap-red: #cc2024;
    --wrap-red-deep: #9e1c20;
    --wrap-charcoal: #2d2c2b;
    --wrap-white: #ffffff;
    --window-grey: #4a4b4f;
    --page-bg: #ffffff;
  }
  html, body {
    margin: 0;
    padding: 0;
    width: 1200px;
    height: 851px;
    overflow: hidden;
    background: var(--page-bg);
  }
  .wrap-sheet {
    display: block;
    width: 1200px;
    height: 851px;
  }
  .service {
    font-family: "Open Sans", Arial, sans-serif;
    font-weight: 700;
    fill: var(--wrap-white);
  }
  .brand-name {
    font-family: "Roboto Condensed", "Arial Narrow", sans-serif;
    font-weight: 400;
    fill: var(--wrap-white);
  }
  .phone {
    font-family: "Roboto Condensed", "Arial Narrow", sans-serif;
    font-weight: 400;
    fill: var(--wrap-white);
    letter-spacing: 0.3px;
  }
  .phone-pill { fill: var(--wrap-charcoal); }
  .red-field { fill: url(#redSweep); }
  .dark-disc { fill: var(--wrap-charcoal); }
  .white-ring { fill: var(--wrap-white); }
  .rule { stroke: #1a1a1a; stroke-width: 1.4; }
  .brand-mark { fill: none; stroke: var(--wrap-white); stroke-width: 2.5; }
  .rear-window { fill: var(--window-grey); }
</style>
</head>
<body>
<svg class="wrap-sheet" viewBox="0 0 1200 851" xmlns="http://www.w3.org/2000/svg">
  <defs>
    <linearGradient id="redSweep" x1="0" y1="0" x2="1" y2="1">
      <stop offset="0" stop-color="#b81e22"/>
      <stop offset="0.45" stop-color="var(--wrap-red)"/>
      <stop offset="1" stop-color="var(--wrap-red-deep)"/>
    </linearGradient>
    <clipPath id="clipCubeLeft"><path d="M251 88 H548 V286 H315 V155 H251 Z"/></clipPath>
    <clipPath id="clipCubeRight"><path d="M651 88 H948 V155 H884 V286 H651 Z"/></clipPath>
    <clipPath id="clipRear"><rect x="784" y="497" width="275" height="287"/></clipPath>
    <clipPath id="clipDoorLeft"><path d="M97 275 Q118 225 175 216 H290 V275 Z"/></clipPath>
    <clipPath id="clipDoorRight"><path d="M1103 275 Q1082 225 1025 216 H910 V275 Z"/></clipPath>
  </defs>

  <!-- Cube, driver side -->
  <g class="cube-side cube-side--driver" clip-path="url(#clipCubeLeft)">
    <rect class="red-field" x="251" y="88" width="297" height="198"/>
    <circle class="white-ring" cx="523" cy="188" r="112"/>
    <circle class="dark-disc" cx="527" cy="188" r="105"/>
    <line class="rule" x1="251" y1="139" x2="421" y2="139"/>
    <line class="rule" x1="315" y1="167" x2="414" y2="167"/>
    <line class="rule" x1="315" y1="195" x2="412" y2="195"/>
    <text class="service" x="417" y="131" font-size="12.5" text-anchor="end">Soundage</text>
    <text class="service" x="405" y="159" font-size="12.5" text-anchor="end">Mecanique</text>
    <text class="service" x="403" y="187" font-size="12.5" text-anchor="end">Line boring</text>
    <rect class="phone-pill" x="326" y="218" width="86" height="19" rx="5"/>
    <text class="phone" x="369" y="233" font-size="12.5" text-anchor="middle">506-817-2296</text>
    <circle class="brand-mark" cx="487" cy="157" r="31"/>
    <text class="brand-name" x="487" y="211" font-size="17" text-anchor="middle">KM Fabworks</text>
  </g>

  <!-- Door, driver side -->
  <g class="door-panel door-panel--driver" clip-path="url(#clipDoorLeft)">
    <rect class="red-field" x="97" y="214" width="193" height="61"/>
    <circle class="white-ring" cx="245" cy="216" r="59"/>
    <rect class="white-ring" x="245" y="157" width="50" height="120"/>
    <circle class="dark-disc" cx="249" cy="216" r="56"/>
    <rect class="dark-disc" x="249" y="160" width="46" height="117"/>
    <text class="service" x="162" y="233" font-size="7.5" text-anchor="middle">Soundage</text>
    <text class="service" x="165" y="246" font-size="7.5" text-anchor="middle">Mecanique</text>
    <text class="service" x="172" y="260" font-size="7.5" text-anchor="middle">Line boring</text>
    <circle class="brand-mark" cx="252" cy="234" r="15" stroke-width="1.6"/>
    <text class="brand-name" x="252" y="264" font-size="8.5" text-anchor="middle">KM Fabworks</text>
  </g>

  <!-- Cube, passenger side -->
  <g class="cube-side cube-side--passenger" clip-path="url(#clipCubeRight)">
    <rect class="red-field" x="651" y="88" width="297" height="198"/>
    <circle class="white-ring" cx="676" cy="188" r="112"/>
    <circle class="dark-disc" cx="672" cy="188" r="105"/>
    <line class="rule" x1="778" y1="139" x2="948" y2="139"/>
    <line class="rule" x1="785" y1="167" x2="884" y2="167"/>
    <line class="rule" x1="787" y1="195" x2="884" y2="195"/>
    <text class="service" x="782" y="131" font-size="12.5">Soundage</text>
    <text class="service" x="794" y="159" font-size="12.5">Mecanique</text>
    <text class="service" x="796" y="187" font-size="12.5">Line boring</text>
    <rect class="phone-pill" x="788" y="218" width="86" height="19" rx="5"/>
    <text class="phone" x="831" y="233" font-size="12.5" text-anchor="middle">506-817-2296</text>
    <circle class="brand-mark" cx="713" cy="157" r="31"/>
    <text class="brand-name" x="713" y="211" font-size="17" text-anchor="middle">KM Fabworks</text>
  </g>

  <!-- Door, passenger side -->
  <g class="door-panel door-panel--passenger" clip-path="url(#clipDoorRight)">
    <rect class="red-field" x="910" y="214" width="193" height="61"/>
    <circle class="white-ring" cx="955" cy="216" r="59"/>
    <rect class="white-ring" x="905" y="157" width="50" height="120"/>
    <circle class="dark-disc" cx="951" cy="216" r="56"/>
    <rect class="dark-disc" x="905" y="160" width="46" height="117"/>
    <text class="service" x="1038" y="233" font-size="7.5" text-anchor="middle">Soundage</text>
    <text class="service" x="1035" y="246" font-size="7.5" text-anchor="middle">Mecanique</text>
    <text class="service" x="1028" y="260" font-size="7.5" text-anchor="middle">Line boring</text>
    <circle class="brand-mark" cx="948" cy="234" r="15" stroke-width="1.6"/>
    <text class="brand-name" x="948" y="264" font-size="8.5" text-anchor="middle">KM Fabworks</text>
  </g>

  <!-- Cube, rear -->
  <g class="cube-rear" clip-path="url(#clipRear)">
    <rect class="red-field" x="784" y="497" width="275" height="287"/>
    <rect class="rear-window" x="857" y="538" width="33" height="61" rx="5"/>
    <rect class="rear-window" x="953" y="537" width="33" height="62" rx="5"/>
    <circle class="white-ring" cx="836" cy="705" r="102"/>
    <rect class="white-ring" x="784" y="705" width="52" height="80"/>
    <circle class="dark-disc" cx="832" cy="708" r="96"/>
    <rect class="dark-disc" x="784" y="708" width="48" height="77"/>
    <line class="rule" x1="930" y1="666" x2="1059" y2="666"/>
    <line class="rule" x1="937" y1="693" x2="1059" y2="693"/>
    <line class="rule" x1="938" y1="720" x2="1059" y2="720"/>
    <text class="service" x="946" y="658" font-size="12">Soundage</text>
    <text class="service" x="957" y="685" font-size="12">Mecanique</text>
    <text class="service" x="959" y="712" font-size="12">Line boring</text>
    <rect class="phone-pill" x="949" y="742" width="84" height="19" rx="5"/>
    <text class="phone" x="991" y="757" font-size="12.5" text-anchor="middle">506-817-2296</text>
    <circle class="brand-mark" cx="856" cy="684" r="36"/>
    <text class="brand-name" x="856" y="744" font-size="18" text-anchor="middle">KM Fabworks</text>
  </g>
</svg>
</body>
</html>
```